Alloy Wheels Wholesaler and Distributor Product Brochure Design

We need product Brochure design.
We are an alloy wheel distributor and need a sophisticated product catalogue/brochure to supply for our clients. Our website is www.trevonrims.com.au so you can have a look and get the idea.
Needs to be professional. I have a base concept of lay out, see attached.
The number of products per page is exactly how I need it, but arrangement and further enhancement to make it look better is what we looking for.
I would like all products to be on white background.

- Size will need to be DL format 98mm x 210mm with 2mm bleed
- Openable Horizontally ( landscape format )
- 12 pages ( see attached page by page guide )
- Final file needs to be print ready,

See files attached:
1. All product photos
2. List of products with names/description
3. Sample lay out of brochure how I see it pay by page
4. our existing logo, also have AI file if requested.
5. Text for second last page ( warranty and care instructions )
6. Some sample photos of vehicle that can be use on front page.

If I missed anything please message.
Updates

Target Market(s)

To be used by retail outlets to showcase the products as well as end clients to keep for their consideration when selecting a wheel for their vehicle.

Industry/Entity Type

Automotive

Colors
0455a3
3176b5
85acd3
ffffff

Requirements
Must have
• Professional look, in line with our general theme and exiting website.
Should not have
• we need it to be simple and minimum colours

```html
<!DOCTYPE html>
<html lang="en">
<head>
<meta charset="utf-8">
<title>Trevonrims Wheel Catalogue – Spread</title>
<link rel="stylesheet" href="https://fonts.googleapis.com/css2?family=Oswald:wght@400;500;600&family=Cinzel:wght@400&display=swap">
<style>
  :root {
    --brand-deep: #0455a3;
    --brand-mid: #3176b5;
    --brand-light: #85acd3;
    --paper: #ffffff;
    --ink: #1a1a1a;
    --rule: #c9c9c9;
    --frame: #9a9a9a;
    --footer-ink: #6d6d6d;
  }
  * { margin: 0; padding: 0; box-sizing: border-box; }
  html, body { width: 1200px; height: 280px; overflow: hidden; background: var(--paper); }
  .spread { position: relative; width: 1200px; height: 280px; background: var(--paper); font-family: "Oswald", sans-serif; color: var(--ink); }
  .page { position: absolute; top: 0; width: 600px; height: 280px; }
  .page--left { left: 0; }
  .page--right { left: 600px; border-left: 1px solid var(--rule); }

  /* Left page: framed product tiles */
  .tile { position: absolute; top: 67px; width: 123px; }
  .tile__frame { width: 123px; height: 123px; border: 1px solid var(--frame); display: flex; align-items: center; justify-content: center; background: var(--paper); }
  .tile__label { margin: 4px auto 0; width: 90px; height: 37px; border-radius: 3px; background: linear-gradient(to bottom, var(--brand-mid), #2a8ad6); color: var(--paper); text-align: center; padding-top: 3px; }
  .tile__name { font-size: 11px; font-weight: 500; letter-spacing: 0.3px; line-height: 12px; }
  .tile__finish { font-size: 5.5px; line-height: 8px; text-transform: uppercase; white-space: nowrap; }
  .tile__sizes { font-size: 5.5px; line-height: 7px; }

  .wheel { border-radius: 50%; }
  .wheel--black { background: radial-gradient(circle at 50% 50%, #bfc4c8 0 7%, #2a2a2a 9%, #151515 40%, #4a4a4a 60%, #111 72%, #2c2c2c 100%); }
  .wheel--machined { background: radial-gradient(circle at 50% 50%, #bfc4c8 0 7%, #1c1c1c 9%, #9a9a9a 35%, #1b1b1b 55%, #cfcfcf 68%, #222 100%); }
  .wheel--titanium { background: radial-gradient(circle at 50% 50%, #d0d4d8 0 7%, #6c6c6c 9%, #b4b4b4 40%, #5f5f5f 62%, #c6c6c6 75%, #555 100%); }
  .wheel--silver { background: radial-gradient(circle at 50% 50%, #e8e8e8 0 7%, #bdbdbd 9%, #e2e2e2 40%, #a8a8a8 62%, #efefef 75%, #9c9c9c 100%); }
  .tile .wheel { width: 92px; height: 100px; }

  /* Right page: wheel with side tag */
  .feature { position: absolute; display: flex; align-items: center; }
  .feature .wheel { width: 82px; height: 80px; flex: none; }
  .feature__backdrop { width: 106px; height: 94px; background: #ececec; display: flex; align-items: center; justify-content: center; flex: none; margin-right: -12px; }
  .tag { position: relative; margin-left: 2px; height: 37px; border: 1px solid #bdbdbd; border-radius: 5px; background: var(--paper); box-shadow: 0 1px 2px rgba(0,0,0,0.15); text-align: center; padding-top: 3px; }
  .tag__name { font-size: 11px; font-weight: 600; line-height: 12px; }
  .tag__finish { font-size: 5.5px; line-height: 8px; text-transform: uppercase; white-space: nowrap; }
  .tag__sizes { font-size: 5.5px; line-height: 7px; }

  .folio { position: absolute; top: 257px; font-family: "Cinzel", serif; font-size: 8px; letter-spacing: 2.6px; color: var(--footer-ink); }
  .page--left .folio { left: 26px; }
  .page--right .folio { right: 26px; }
</style>
</head>
<body>
<main class="spread">
  <section class="page page--left">
    <article class="tile" style="left:22px">
      <div class="tile__frame"><div class="wheel wheel--black" role="img" aria-label="Product photo of the Sabre wheel in satin black"></div></div>
      <div class="tile__label"><p class="tile__name">SABRE</p><p class="tile__finish">Satin Black</p><p class="tile__sizes">19x8, 20x9</p></div>
    </article>
    <article class="tile" style="left:166px">
      <div class="tile__frame"><div class="wheel wheel--machined" role="img" aria-label="Product photo of the Sabre wheel in satin black with machined face"></div></div>
      <div class="tile__label"><p class="tile__name">SABRE</p><p class="tile__finish">Satin Black/ Machined</p><p class="tile__sizes">19x8, 20x9</p></div>
    </article>
    <article class="tile" style="left:310px">
      <div class="tile__frame"><div class="wheel wheel--titanium" role="img" aria-label="Product photo of the Sabre wheel in titanium grey with machined face"></div></div>
      <div class="tile__label"><p class="tile__name">SABRE</p><p class="tile__finish">Titanium Grey / Machined</p><p class="tile__sizes">19x8, 20x9</p></div>
    </article>
    <article class="tile" style="left:454px">
      <div class="tile__frame"><div class="wheel wheel--silver" role="img" aria-label="Product photo of the Sabre wheel in silver with machined face"></div></div>
      <div class="tile__label"><p class="tile__name">SABRE</p><p class="tile__finish">Silver / Machined</p><p class="tile__sizes">19x8, 20x9</p></div>
    </article>
    <p class="folio">www.trevonrims.com.au</p>
  </section>

  <section class="page page--right">
    <article class="feature" style="left:74px; top:30px">
      <div class="wheel wheel--black" role="img" aria-label="Product photo of the Vector wheel in satin black"></div>
      <div class="tag" style="width:86px"><p class="tag__name">VECTOR</p><p class="tag__finish">Satin Black</p><p class="tag__sizes">18x8, 19x8</p></div>
    </article>
    <article class="feature" style="left:342px; top:30px">
      <div class="wheel wheel--silver" role="img" aria-label="Product photo of the Vector wheel in hyper silver"></div>
      <div class="tag" style="width:90px"><p class="tag__name">VECTOR</p><p class="tag__finish">Hyper Silver</p><p class="tag__sizes">18x8, 19x8</p></div>
    </article>
    <article class="feature" style="left:74px; top:158px">
      <div class="wheel wheel--machined" role="img" aria-label="Product photo of the Vortex wheel in satin black with machined face"></div>
      <div class="tag" style="width:86px; height:40px"><p class="tag__name">VORTEX</p><p class="tag__finish">Satin Black/ Machined</p><p class="tag__sizes">18x8, 19x8.5</p></div>
    </article>
    <article class="feature" style="left:332px; top:152px">
      <div class="feature__backdrop"><div class="wheel wheel--titanium" role="img" aria-label="Product photo of the Vortex wheel in titanium grey with machined face"></div></div>
      <div class="tag" style="width:90px; height:40px"><p class="tag__name">VORTEX</p><p class="tag__finish">Titanium Grey / Machined</p><p class="tag__sizes">18x8, 19x8.5</p></div>
    </article>
    <p class="folio">www.trevonrims.com.au</p>
  </section>
</main>
</body>
</html>
```